Business Card *

A business card design
Use the logo uploaded in the brief page.
You may use placeholders in your design layouts.
I will provide the actual business card details to the winning designer.

Logo
Place for contact info (name, title, phone, email, etc)

Requirements
Must have
• Logo

```html
<!DOCTYPE html>
<html lang="en">
<head>
<meta charset="utf-8">
<title>Ridgeway Business Card</title>
<link rel="stylesheet" href="https://fonts.googleapis.com/css2?family=Poppins:wght@300;400;600;700&display=swap">
<style>
  :root {
    --stage: #e9e7e3;
    --card-white: #f1f1f1;
    --back-grey-light: #b3b3b3;
    --back-grey-dark: #8a8a8a;
    --brand-green: #3fbf4f;
    --text-grey: #8f8f8f;
    --white: #ffffff;
  }
  * { box-sizing: border-box; margin: 0; padding: 0; }
  html, body { width: 1200px; height: 780px; overflow: hidden; }
  body {
    background: var(--stage);
    font-family: "Poppins", sans-serif;
    position: relative;
  }
  .card {
    position: absolute;
    top: 230px;
    width: 560px;
    height: 320px;
    border-radius: 18px;
    overflow: hidden;
    box-shadow: 0 6px 18px rgba(0,0,0,0.18);
  }
  .card-front { left: 25px; background: var(--card-white); }
  .card-back {
    left: 615px;
    background: radial-gradient(ellipse at 40% 30%, var(--back-grey-light), var(--back-grey-dark));
  }
  .front-swoosh { position: absolute; inset: 0; }
  .holder {
    position: absolute;
    top: 18px;
    right: 30px;
    text-align: right;
    color: var(--white);
  }
  .holder-name { font-weight: 600; font-size: 17px; letter-spacing: 0.5px; line-height: 22px; }
  .holder-title { font-weight: 300; font-size: 12px; line-height: 16px; }
  .brand {
    position: absolute;
    left: 122px;
    top: 182px;
    display: flex;
    align-items: center;
    gap: 9px;
  }
  .brand-dot {
    width: 20px; height: 20px;
    border-radius: 50%;
    background: var(--brand-green);
  }
  .brand-name {
    font-weight: 700;
    font-size: 26px;
    line-height: 34px;
    letter-spacing: 1px;
    color: var(--text-grey);
  }
  .rule {
    position: absolute;
    left: 122px;
    top: 224px;
    width: 400px;
    height: 1px;
    background: var(--brand-green);
  }
  .contacts {
    position: absolute;
    left: 122px;
    top: 234px;
    list-style: none;
    color: var(--text-grey);
    font-size: 12px;
    font-weight: 300;
    line-height: 24px;
  }
  .contacts li { display: flex; align-items: center; gap: 9px; }
  .contact-icon {
    width: 15px; height: 15px;
    border: 2px solid var(--brand-green);
    border-radius: 50%;
    display: inline-flex; align-items: center; justify-content: center;
  }
  .contact-icon::after {
    content: ""; width: 5px; height: 5px;
    background: var(--brand-green); border-radius: 1px;
  }
  .contact-web { font-weight: 600; }
  .divider {
    position: absolute;
    left: 336px;
    top: 240px;
    width: 1px;
    height: 56px;
    background: var(--brand-green);
  }
  .address {
    position: absolute;
    left: 352px;
    top: 246px;
    color: var(--text-grey);
    font-size: 12px;
    font-weight: 300;
    font-style: normal;
    line-height: 22px;
  }
  .back-brand {
    position: absolute;
    inset: 0;
    display: flex;
    align-items: center;
    justify-content: center;
    gap: 14px;
  }
  .back-brand .brand-dot { width: 30px; height: 30px; background: var(--white); }
  .back-brand .brand-name { color: var(--white); font-size: 40px; line-height: 50px; }
</style>
</head>
<body>
  <section class="card card-front" aria-label="Business card front">
    <svg class="front-swoosh" width="560" height="320" viewBox="0 0 560 320" aria-hidden="true">
      <defs>
        <linearGradient id="bandShade" x1="0" y1="0" x2="1" y2="1">
          <stop offset="0" stop-color="#9d9d9d"/>
          <stop offset="1" stop-color="#b8b8b8"/>
        </linearGradient>
      </defs>
      <path d="M0,0 H560 V70 C200,80 30,150 30,320 H0 Z" fill="url(#bandShade)"/>
      <path d="M30,320 C30,150 200,80 560,70" transform="translate(4,4)" fill="none" stroke="#fafafa" stroke-width="9"/>
      <path d="M30,320 C30,150 200,80 560,70" transform="translate(9,9)" fill="none" stroke="#3fbf4f" stroke-width="4"/>
    </svg>

    <div class="holder">
      <p class="holder-name">DANIEL R. HALE</p>
      <p class="holder-title">Executive Director</p>
    </div>

    <div class="brand">
      <span class="brand-dot"></span>
      <span class="brand-name">RIDGEWAY</span>
    </div>

    <div class="rule"></div>

    <ul class="contacts">
      <li><span class="contact-icon"></span>555-210-4821</li>
      <li><span class="contact-icon"></span>hello@ridgewaymail.com</li>
      <li><span class="contact-icon"></span><span class="contact-web">www.ridgewayfields.com</span></li>
    </ul>

    <div class="divider"></div>

    <address class="address">
      PO BOX 482 Meadow Lane<br>
      Cedar Falls, Iowa, USA
    </address>
  </section>

  <section class="card card-back" aria-label="Business card back">
    <div class="back-brand">
      <span class="brand-dot"></span>
      <span class="brand-name">RIDGEWAY</span>
    </div>
  </section>
</body>
</html>
```